Halvercott Orthodontics business card

Using our existing logo (created with ArtFolio), please create a tasteful, contemporary business card. We are father and daughter orthodontists specializing in braces, clarafit, etc to design healthy, beautiful smiles for children, adolescents, and adults. We would like the design to be family-friendly but not childish.
The final design should include all of the information without looking cluttered (I hope! If necessary to achieve an optimal design, please consider making the card double-sided)
Purple, black, silver on a white card
Please include the following information:
Halvercott Orthodontics (logo)
Marguerite L. Halvercott, DMD
Douglas R. Halvercott, DMD

312 Bramblewood Street
North Andover, MA 01899
978.555.0142

847C Quarry Hollow Street
Methuen, MA 01898
978.555.0187

email frontdesk@halvercottortho.example
website www.halvercottortho.example

```html
<!DOCTYPE html>
<html lang="en">
<head>
<meta charset="utf-8">
<title>Halvercott Orthodontics – Business Card</title>
<link rel="stylesheet" href="https://fonts.googleapis.com/css2?family=Montserrat:wght@500;600&display=swap">
<style>
  :root {
    --backdrop: #e6e7e6;
    --card: #ffffff;
    --purple: #6b2f90;
    --lavender: #d2cfdf;
    --silver-light: #ebebee;
    --silver: #8a8a8a;
    --text-grey: #8a8a8a;
  }
  * { margin: 0; padding: 0; box-sizing: border-box; }
  html, body {
    width: 1200px;
    height: 1200px;
    overflow: hidden;
    background: var(--backdrop);
    font-family: "Montserrat", Arial, sans-serif;
  }
  .business-card {
    position: absolute;
    left: 100px;
    top: 307px;
    width: 980px;
    height: 561px;
    background: var(--card);
    overflow: hidden;
  }
  .card-bands {
    position: absolute;
    inset: 0;
    width: 980px;
    height: 561px;
  }
  .brand {
    position: absolute;
    left: 190px;
    top: 226px;
    display: flex;
    align-items: center;
    gap: 26px;
  }
  .brand-dot {
    width: 70px;
    height: 70px;
    border-radius: 50%;
    background: var(--purple);
    flex: none;
  }
  .brand-name {
    color: var(--purple);
    font-weight: 500;
    line-height: 1;
  }
  .brand-name .practice {
    display: block;
    font-size: 58px;
    letter-spacing: 0.02em;
  }
  .brand-name .specialty {
    display: block;
    margin-top: 12px;
    font-size: 28px;
    letter-spacing: 0.36em;
  }
  .doctors {
    position: absolute;
    right: 39px;
    top: 435px;
    text-align: right;
    color: var(--text-grey);
    font-weight: 600;
    font-size: 22px;
    line-height: 33px;
  }
</style>
</head>
<body>
  <div class="business-card">
    <svg class="card-bands" viewBox="0 0 980 561" aria-hidden="true">
      <polygon points="0,0 980,0 980,9 826,94 0,7" fill="var(--silver-light)"/>
      <polygon points="0,0 980,0 980,4 820,85 0,4" fill="var(--lavender)"/>
      <polygon points="0,553 227,479 980,556 980,561 0,561" fill="var(--silver)"/>
      <polygon points="0,557 227,494 980,561 0,561" fill="var(--purple)"/>
    </svg>

    <div class="brand">
      <span class="brand-dot"></span>
      <div class="brand-name">
        <span class="practice">HALVERCOTT</span>
        <span class="specialty">ORTHODONTICS</span>
      </div>
    </div>

    <div class="doctors">
      <p>Marguerite L. Halvercott, DMD</p>
      <p>Douglas R. Halvercott, DMD</p>
    </div>
  </div>
</body>
</html>
```